Fireworks company

COLORFUL design, incorporating logo (attached).
Information to be included:
PO BOX 4827
Highton Victoria 3381
Ph 03 5461 2839
Fax 03 5487 9016
Email sales@halbrenncelebrations.com.au
Web www.halbrenncelebrations.com.au

Check out our website for more inspiration? :-)

```html
<!DOCTYPE html>
<html lang="en">
<head>
<meta charset="utf-8">
<title>Halbrenn Celebrations Letterhead</title>
<link href="https://fonts.googleapis.com/css2?family=Roboto+Slab:wght@700;800&display=swap" rel="stylesheet">
<style>
  :root {
    --ink: #000000;
    --paper: #ffffff;
    --brand-orange: #f07a1c;
    --label-red: #e8263a;
    --dot-yellow: #f2d21a;
    --stripe-grey: #8a8a8a;
    --wave-deep: #f06a00;
    --wave-light: #ffb347;
  }
  * { margin: 0; padding: 0; box-sizing: border-box; }
  html, body { width: 847px; height: 1200px; overflow: hidden; background: var(--paper); }
  .letterhead {
    position: relative;
    width: 847px;
    height: 1200px;
    background: var(--paper);
    font-family: "Roboto Slab", Georgia, serif;
  }
  .masthead {
    position: absolute;
    inset: 0 0 auto 0;
    height: 210px;
    background: var(--ink);
    overflow: hidden;
  }
  .masthead__photo {
    position: absolute;
    top: 0;
    height: 210px;
  }
  .masthead__photo--left {
    left: 0;
    width: 230px;
    background: radial-gradient(circle at 40% 35%, #e83a2a 0%, #8a1410 30%, #1a0302 60%, #000 80%);
  }
  .masthead__photo--right {
    right: 0;
    width: 270px;
    background: radial-gradient(ellipse at 55% 55%, #ffd9d0 0%, #e8283a 25%, #5a0a12 50%, #000 75%);
  }
  .brand {
    position: absolute;
    top: 26px;
    left: 0;
    right: 0;
    display: flex;
    align-items: center;
    justify-content: center;
    gap: 14px;
  }
  .brand__name {
    color: var(--brand-orange);
    font-weight: 800;
    font-size: 36px;
    line-height: 40px;
    letter-spacing: 1px;
    text-align: center;
  }
  .brand__mark {
    width: 14px;
    height: 14px;
    border-radius: 50%;
    background: var(--dot-yellow);
  }
  .contact {
    position: absolute;
    top: 122px;
    left: 0;
    right: 0;
    text-align: center;
    color: var(--paper);
    font-style: normal;
    font-weight: 700;
    font-size: 13px;
    line-height: 22px;
  }
  .contact__label { color: var(--label-red); }
  .contact__sep { color: var(--dot-yellow); padding: 0 6px; }
  .rule-stripes {
    position: absolute;
    top: 210px;
    left: 0;
    width: 847px;
    height: 24px;
  }
  .footer-wave {
    position: absolute;
    left: 0;
    bottom: 0;
    width: 847px;
    height: 150px;
  }
</style>
</head>
<body>
<main class="letterhead">
  <header class="masthead">
    <div class="masthead__photo masthead__photo--left" role="img" aria-label="Photo of red and gold fireworks bursting in the night sky"></div>
    <div class="masthead__photo masthead__photo--right" role="img" aria-label="Photo of a red fireworks display over water at night"></div>
    <div class="brand">
      <span class="brand__name">HALBRENN<br>CELEBRATIONS</span>
      <span class="brand__mark"></span>
    </div>
    <address class="contact">
      <div>PO BOX 4827<span class="contact__sep">•</span>Tarrow Heights, Aldermere 3381</div>
      <div><span class="contact__label">Phone:</span> (03) 5461 2839<span class="contact__sep">•</span><span class="contact__label">Fax:</span> (03) 5487 9016</div>
      <div><span class="contact__label">Email:</span> sales@halbrenncelebrations.com.au<span class="contact__sep">•</span><span class="contact__label">Web:</span> www.halbrenncelebrations.com.au</div>
    </address>
  </header>

  <svg class="rule-stripes" viewBox="0 0 847 24" aria-hidden="true">
    <rect x="0" y="0" width="847" height="4" fill="#000"/>
    <rect x="0" y="6" width="847" height="3" fill="var(--stripe-grey)"/>
    <rect x="0" y="11" width="847" height="3" fill="#000"/>
    <rect x="0" y="16" width="847" height="2" fill="var(--stripe-grey)"/>
    <rect x="0" y="20" width="847" height="2" fill="#000"/>
  </svg>

  <svg class="footer-wave" viewBox="0 0 847 150" preserveAspectRatio="none" aria-hidden="true">
    <defs>
      <linearGradient id="waveFill" x1="0" y1="0" x2="0" y2="1">
        <stop offset="0" stop-color="var(--wave-light)"/>
        <stop offset="1" stop-color="var(--wave-deep)"/>
      </linearGradient>
    </defs>
    <path d="M0 40 Q 420 80 847 10 L847 150 L0 150 Z" fill="url(#waveFill)"/>
    <path d="M0 55 Q 420 95 847 25 L847 35 Q 420 105 0 65 Z" fill="#ffffff" opacity="0.55"/>
    <path d="M0 78 Q 420 118 847 48 L847 150 L0 150 Z" fill="var(--wave-deep)" opacity="0.6"/>
  </svg>
</main>
</body>
</html>
```